Business Card Design for Small Electrical Contractor

I need to update my business card into something a little more modern. We are a small electrical contracting company. We service domestic and commercial places around Sydney. We have 2 logo designs at the moment. I have uploaded both and 2 different sizes to work with.

Industry/Entity Type

Business

Contact Information for Business Card

Leo Hartigan
8/21-23 Birch Rd, Kelsworth 2087
t - (02) 9381 4720
m - 0427 815 903
E - info@hartiganelx.com.au
W - hartiganelx.com.au
ABN: 42 907 551 316

Font styles to use
Sans Serif

Requirements
Must have
• I would also like to see the below fit on somewhere aswell
• - Licensed Electrician
• - Level 2 (Cat 1 & 4)
• - Domestic
• - Commercial
• - Repairs and Installations
• - Data
Nice to have
• Try and keep similar colours as logo
Should not have
• No lightning bolts or light globes. Smart and professional please.

```html
<!DOCTYPE html>
<html lang="en">
<head>
<meta charset="utf-8">
<title>Hartigan Electrical – Business Cards</title>
<link rel="stylesheet" href="https://fonts.googleapis.com/css2?family=Montserrat:wght@400;500;600;700&display=swap">
<style>
  :root {
    --stage: #2b2b2b;
    --card: #050505;
    --orange: #f7962a;
    --white: #ffffff;
    --grey-line: #7a7a7a;
    --text: #f2f2f2;
  }
  * { margin: 0; padding: 0; box-sizing: border-box; }
  html, body { width: 1200px; height: 900px; overflow: hidden; }
  body {
    background: var(--stage);
    font-family: "Montserrat", sans-serif;
    color: var(--text);
    position: relative;
  }
  .card {
    position: absolute;
    top: 285px;
    width: 540px;
    height: 330px;
    border-radius: 18px;
    background: var(--card);
    overflow: hidden;
    box-shadow: 0 12px 30px rgba(0,0,0,.45);
  }
  .card--services { left: 40px; }
  .card--contact { left: 620px; }
  .card__swoosh { position: absolute; inset: 0; width: 100%; height: 100%; }

  .brand {
    position: absolute;
    font-weight: 600;
    font-size: 30px;
    line-height: 1.05;
    color: var(--white);
    letter-spacing: .5px;
  }
  .card--services .brand { left: 40px; top: 52px; }
  .card--contact .brand { right: 40px; top: 60px; text-align: right; }

  .services__web {
    position: absolute; left: 40px; top: 150px;
    font-size: 13px; font-weight: 500;
  }
  .services__list {
    position: absolute; left: 40px; top: 180px;
    list-style: none; font-size: 13px; line-height: 19px;
  }
  .services__list li::before {
    content: ""; display: inline-block;
    width: 6px; height: 6px; border-radius: 50%;
    background: var(--orange); margin-right: 9px; vertical-align: middle;
  }

  .rule {
    position: absolute; height: 1px; background: var(--grey-line);
  }
  .rule--divider { left: 36px; right: 40px; top: 238px; }

  .business-id {
    position: absolute; right: 40px; top: 250px;
    text-align: right; font-size: 12px; line-height: 18px;
  }
  .business-id__label { color: var(--orange); }

  .contact__name {
    position: absolute; left: 36px; top: 204px;
    font-size: 24px; font-weight: 700; color: var(--white);
  }
  .contact__name .first { color: var(--orange); font-weight: 600; }
  .contact__list {
    position: absolute; left: 36px; top: 246px;
    list-style: none; font-size: 12.5px; line-height: 17px;
  }
  .contact__list li { display: flex; align-items: center; gap: 9px; }
  .contact__list svg { width: 11px; height: 11px; flex: none; }
  .accent { color: var(--orange); }
</style>
</head>
<body>

<section class="card card--services">
  <svg class="card__swoosh" viewBox="0 0 540 330" aria-hidden="true">
    <path d="M438 0 C430 170 330 290 232 330 L540 330 L540 0 Z" fill="var(--white)"/>
    <path d="M452 0 C446 175 350 292 256 330 L540 330 L540 0 Z" fill="var(--orange)"/>
  </svg>
  <div class="brand">Hartigan<br>Electrical</div>
  <p class="services__web">www.hartiganelx.com.au</p>
  <ul class="services__list">
    <li>Licensed Electrician</li>
    <li>Level 2 (Cat 1 &amp; 4)</li>
    <li>Domestic</li>
    <li>Commercial</li>
    <li>Repairs and Installations</li>
    <li>Data</li>
  </ul>
</section>

<section class="card card--contact">
  <svg class="card__swoosh" viewBox="0 0 540 330" aria-hidden="true">
    <path d="M228 0 Q64 50 0 192 L0 0 Z" fill="var(--white)"/>
    <path d="M204 0 Q50 42 0 174 L0 0 Z" fill="var(--orange)"/>
  </svg>
  <div class="brand">Hartigan<br>Electrical</div>

  <p class="contact__name"><span class="first">Leo</span> Hartigan</p>
  <div class="rule rule--divider"></div>

  <div class="business-id">
    <p><span class="business-id__label">ABN:</span> 42 907 551 316</p>
    <p>8/21-23 Birch Rd</p>
    <p>Kelsworth 2087</p>
  </div>

  <ul class="contact__list">
    <li>
      <svg viewBox="0 0 12 12" aria-label="Phone"><path d="M2.5 1h2l1 2.6-1.3 1a6 6 0 0 0 3.2 3.2l1-1.3L11 7.5v2a1 1 0 0 1-1 1A9 9 0 0 1 1.5 2a1 1 0 0 1 1-1z" fill="var(--orange)"/></svg>
      (02) 9381 4720
    </li>
    <li>
      <svg viewBox="0 0 12 12" aria-label="Mobile"><rect x="3" y="0.8" width="6" height="10.4" rx="1.2" fill="none" stroke="var(--orange)" stroke-width="1.3"/></svg>
      0427 815 903
    </li>
    <li>
      <svg viewBox="0 0 12 12" aria-label="Email"><rect x="0.8" y="2.3" width="10.4" height="7.4" rx="1" fill="none" stroke="var(--orange)" stroke-width="1.2"/><path d="M1 2.8 6 6.6 11 2.8" fill="none" stroke="var(--orange)" stroke-width="1.2"/></svg>
      info@hartiganelx.com.au
    </li>
    <li>
      <svg viewBox="0 0 12 12" aria-label="Website"><circle cx="6" cy="6" r="5" fill="none" stroke="var(--orange)" stroke-width="1.2"/><path d="M1 6h10M6 1c-2.6 3-2.6 7 0 10M6 1c2.6 3 2.6 7 0 10" fill="none" stroke="var(--orange)" stroke-width="1"/></svg>
      <span>www.<span class="accent">hartiganelx</span>.com.au</span>
    </li>
  </ul>
</section>

</body>
</html>
```